Spices producer needs product label design.

I need a two label design of 90mm(H) x 60mm(H) for multiple line of spices and other product. First label for the front should have the logo, and second label should be the same as the first but without the logo. I would like the same dark reddish colour on my logo for the design if possible or similar. This label will be use for multiple products, so a clear in-between space is important to add information and change product name for printing . I would prefer a mixture of traditional and rustic style.
I have attached my logos and sample on how I would like the look.

Target Market(s)

25-60 women and men.

Industry/Entity Type

Retail

Requirements
Must have
• As stated above.
Nice to have
• Please see attached sample .
Should not have
• Multiple colours, animation design.

```html
<!DOCTYPE html>
<html lang="en">
<head>
<meta charset="utf-8">
<title>Spice Label Set</title>
<link rel="stylesheet" href="https://fonts.googleapis.com/css2?family=Dancing+Script:wght@500;600&display=swap">
<style>
  :root {
    --label-red: #8e1622;
    --label-red-deep: #7a111b;
    --leaf-tint: #a8403f;
    --leaf-gold: #b8614f;
    --band-blue: #bfe0f6;
    --paper-white: #ffffff;
    --canvas-bg: #ffffff;
  }
  html, body {
    margin: 0;
    padding: 0;
    overflow: hidden;
    background: var(--canvas-bg);
  }
  .canvas {
    position: relative;
    width: 1200px;
    height: 1114px;
    background: var(--canvas-bg);
    overflow: hidden;
  }
  .label {
    position: absolute;
    top: 380px;
    width: 530px;
    height: 355px;
  }
  .label--front { left: 50px; }
  .label--back { left: 620px; }
  .label svg { display: block; width: 100%; height: 100%; }
  .label-text {
    font-family: "Dancing Script", cursive;
    font-weight: 600;
    fill: var(--label-red);
  }
  .label-text--brand { font-size: 84px; }
  .label-text--product { font-size: 66px; }
</style>
</head>
<body>
<main class="canvas">

  <svg width="0" height="0" aria-hidden="true" style="position:absolute">
    <defs>
      <linearGradient id="leaf-field-tone" x1="0" y1="0" x2="1" y2="1">
        <stop offset="0" stop-color="var(--leaf-tint)"/>
        <stop offset="0.35" stop-color="var(--label-red)"/>
        <stop offset="0.65" stop-color="var(--leaf-tint)"/>
        <stop offset="1" stop-color="var(--label-red-deep)"/>
      </linearGradient>
      <radialGradient id="leaf-field-glow" cx="0.5" cy="0.5" r="0.75">
        <stop offset="0" stop-color="var(--leaf-gold)" stop-opacity="0.18"/>
        <stop offset="1" stop-color="var(--leaf-gold)" stop-opacity="0"/>
      </radialGradient>
    </defs>
  </svg>

  <section class="label label--front" aria-label="Front label with brand name">
    <svg viewBox="0 0 530 355" xmlns="http://www.w3.org/2000/svg">
      <rect class="band-blue" x="0" y="0" width="530" height="14" fill="var(--band-blue)"/>
      <g class="leaf-field" role="img" aria-label="Dark red field with a repeating pattern of fine outlined bay leaf sprigs in soft gold">
        <rect x="0" y="14" width="530" height="327" fill="url(#leaf-field-tone)"/>
        <rect x="0" y="14" width="530" height="327" fill="url(#leaf-field-glow)"/>
      </g>
      <rect class="band-blue" x="0" y="341" width="530" height="14" fill="var(--band-blue)"/>
      <rect class="band-white" x="0" y="162" width="530" height="32" fill="var(--paper-white)"/>
      <ellipse class="name-plate" cx="265" cy="178" rx="168" ry="78"
               fill="var(--paper-white)" stroke="var(--label-red)" stroke-width="6"/>
      <text class="label-text label-text--brand" x="265" y="204" text-anchor="middle">Tarvo</text>
    </svg>
  </section>

  <section class="label label--back" aria-label="Product label without brand name">
    <svg viewBox="0 0 530 355" xmlns="http://www.w3.org/2000/svg">
      <rect class="band-blue" x="0" y="0" width="530" height="14" fill="var(--band-blue)"/>
      <g class="leaf-field" role="img" aria-label="Dark red field with a repeating pattern of fine outlined bay leaf sprigs in soft gold">
        <rect x="0" y="14" width="530" height="327" fill="url(#leaf-field-tone)"/>
        <rect x="0" y="14" width="530" height="327" fill="url(#leaf-field-glow)"/>
      </g>
      <rect class="band-blue" x="0" y="341" width="530" height="14" fill="var(--band-blue)"/>
      <rect class="band-white" x="0" y="162" width="530" height="32" fill="var(--paper-white)"/>
      <ellipse class="name-plate" cx="265" cy="178" rx="168" ry="78"
               fill="var(--paper-white)" stroke="var(--label-red)" stroke-width="6"/>
      <text class="label-text label-text--product" x="278" y="170" text-anchor="middle">Bay</text>
      <text class="label-text label-text--product" x="252" y="226" text-anchor="middle">Leaves</text>
    </svg>
  </section>

</main>
</body>
</html>
```